Aviation Consulting Firm Needs Website Redesign

Job Type
Web Design (Coded - Design and coding required)

Task Outline
Create a Web Design (Coded - Design and coding required)
Designer must provide full implementation/coding depending on the platform chosen by the client (i.e. Wordpress theme, HTML/CSS, etc.) and uploaded to my hosting site (HostLumo).

We are looking to revisit our existing website. Looking for concepts and designs for how the website might look, flow and feel. Current website is: http://www.qelvora-air.example/

QVLx7 is an industry leader in providing solutions for airlines, air traffic control and communities. We improve airport efficiency and reduce costs for stake holders while remaining environmentally friendly and conscious of community concerns.

Scope and Deliverables: Concept design for the home page and internal pages. Pages we need: Home, Industry Specialties, Solutions, Case Studies & Testimonials, Blog, and Contact Us.

We understand that the pages, other then home, will be fairly empty, but need to have each page have a unified theme.

We would love to see a design feature based on our name, logo, or industry, which can run through banners and other collateral (twitter banner, ads on Google, corporate documents etc).

We want the brand to properly depict what we bring/deliver to businesses when consulting to them and this should extend to the color scheme, logo, and font.

Our brand should suitably communicate our ability, knowledge and extensive experience providing aviation solutions.

It should express and evoke credibility, knowledge and understanding of the aviation industry, reliability, efficiency, trust, expertise, approach ability, service delivery but be uncomplicated, practical and use plain speaking language.

Colors that reinforce this might include: Reds, blacks, silver, white, and grey.

Target Market(s)

Aviation Industry - Both domestic and international airlines, airports, and governments

Industry/Entity Type

Aviation

Coding

Coded - Design and coding required

Number of Pages Required

5+ page

Font styles to use
Sans Serif

Colors
ec1f27

Requirements
Must have
• This is a full site, must be coded and moved to our host site.

```html
<!DOCTYPE html>
<html lang="en">
<head>
<meta charset="utf-8">
<title>QVLx7 – Aviation Solutions</title>
<link rel="stylesheet" href="https://fonts.googleapis.com/css2?family=Lato:ital,wght@0,400;0,700;0,900;1,400&family=Raleway:wght@300;400;700&display=swap">
<style>
:root{
  --red:#ec1f27;
  --dark:#353535;
  --darker:#222222;
  --footer:#1f1f1f;
  --text:#333333;
  --muted:#555555;
  --line:#d6d6d6;
  --white:#ffffff;
}
*{box-sizing:border-box;margin:0;padding:0}
html,body{width:818px;height:1200px;overflow:hidden}
body{font-family:"Lato",sans-serif;color:var(--text);background:var(--white);position:relative}
.wrap{width:640px;margin:0 auto;position:relative}

/* header */
.site-header{height:95px;background:linear-gradient(#f4f4f4,#ffffff);position:relative}
.brand{position:absolute;left:93px;top:0;width:123px;height:89px;background:#fff;border-radius:0 0 6px 6px;box-shadow:0 1px 4px rgba(0,0,0,.25);display:flex;flex-direction:column;align-items:center;justify-content:center;gap:6px}
.brand-name{font-family:"Lato",sans-serif;font-weight:700;font-size:22px;color:var(--darker);display:flex;align-items:center;gap:6px}
.brand-name i{width:8px;height:8px;background:var(--red);border-radius:50%;display:block}
.brand-sub{font-size:6.5px;border:1px solid #222;padding:1px 3px;color:#222}
.phone{position:absolute;right:88px;top:14px;font-size:12.5px;font-weight:700;display:flex;align-items:center;gap:6px;color:var(--darker)}
.main-nav{position:absolute;right:87px;top:52px;display:flex;align-items:center;font-size:12px}
.main-nav a{color:var(--darker);text-decoration:none;padding:0 8px;border-left:1px solid #ccc;line-height:13px}
.main-nav a.active{background:var(--red);color:#fff;border:none;padding:5px 8px;line-height:12px;margin-right:5px}
.main-nav a.active+a{border-left:none}

/* hero */
.hero{height:257px;position:relative;background:linear-gradient(180deg,#5f7fa8 0%,#9cb4cf 35%,#6b7482 65%,#2b2d33 100%)}
.hero-caption{position:absolute;left:104px;top:206px;font-family:"Raleway",sans-serif;font-weight:400;font-size:19px;line-height:22px;color:#fff}
.dots{position:absolute;left:665px;top:225px;display:flex;gap:3px}
.dots span{width:9px;height:9px;border:1.5px solid #fff;border-radius:50%}
.dots span.on{background:var(--red);border-color:var(--red)}

/* welcome */
.welcome{height:200px;position:relative}
.welcome-text{position:absolute;left:90px;top:17px;width:365px}
.section-title{font-family:"Raleway",sans-serif;font-weight:400;font-size:21px;color:var(--darker);padding-bottom:6px;border-bottom:1px solid var(--line)}
.section-title b{color:var(--red);font-weight:700}
.lead{font-size:9.5px;font-weight:700;margin:10px 0 12px}
.welcome-text p.body{font-size:9.5px;line-height:15.5px;color:var(--muted)}
.btn-red{display:inline-block;background:var(--red);color:#fff;font-size:10px;font-weight:700;padding:4px 7px;margin-top:13px}
.video{position:absolute;left:504px;top:21px;width:226px;height:152px;border:1px solid #222;background:linear-gradient(180deg,#8a5a2a,#e0791a 45%,#5c3213 80%,#1c1c1c);box-shadow:0 3px 6px rgba(0,0,0,.3)}
.play{position:absolute;left:98px;top:55px;width:36px;height:26px;background:rgba(20,20,20,.8);border-radius:5px}
.play::after{content:"";position:absolute;left:14px;top:7px;border-left:10px solid #fff;border-top:6px solid transparent;border-bottom:6px solid transparent}
.controls{position:absolute;left:0;right:0;bottom:0;height:16px;background:#1b1b1b;display:flex;align-items:center;padding:0 6px;gap:8px}
.bar{flex:1;height:3px;background:#555;border-radius:2px;position:relative}
.bar i{position:absolute;left:0;top:0;height:3px;width:48%;background:var(--red)}

/* services */
.services{height:129px;background:var(--dark);position:relative;color:#fff}
.services-title{position:absolute;left:103px;top:28px;font-family:"Raleway",sans-serif;font-size:30px;line-height:38px;font-weight:300}
.services-title b{font-weight:700;display:block}
.svc-divider{position:absolute;top:19px;width:1px;height:89px;background:#555}
.svc{position:absolute;top:19px;text-align:center;font-size:12.5px;font-weight:700;line-height:15.5px}
.svc-icon{width:52px;height:52px;border:1.5px solid #888;border-radius:50%;margin:0 auto 12px;display:flex;align-items:center;justify-content:center}

/* inquiry */
.inquiry{height:97px;background:var(--red);position:relative}
.inquiry h2{position:absolute;left:91px;top:14px;font-family:"Raleway",sans-serif;font-weight:400;font-size:20px;color:#fff}
.inquiry h2 b{font-weight:700}
.field{position:absolute;top:50px;height:29px;background:#fff;font-size:10px;color:#888;padding:8px 8px}
.submit{position:absolute;left:593px;top:50px;width:136px;height:29px;background:var(--darker);color:#fff;font-family:"Raleway",sans-serif;font-weight:700;font-size:15px;text-align:center;line-height:29px}

/* blog & testimonials */
.lower{height:242px;position:relative}
.col-head{position:absolute;top:22px;height:28px;border-bottom:1px solid var(--line);font-family:"Raleway",sans-serif;font-size:20px;color:var(--darker);display:flex;align-items:center;gap:8px}
.col-head b{color:var(--red);font-weight:700}
.arrows{position:absolute;right:0;top:6px;font-size:15px;color:#777;letter-spacing:5px}
.post{position:absolute;left:90px;width:298px;height:74px}
.thumb{position:absolute;left:0;top:0;width:75px;height:62px;border:2px solid #fff;box-shadow:0 0 2px rgba(0,0,0,.4)}
.post h4{position:absolute;left:88px;top:0;font-size:8.8px;font-weight:700;color:var(--darker)}
.post .date{position:absolute;left:88px;top:14px;font-size:8.5px;font-weight:700;color:var(--red)}
.post p{position:absolute;left:88px;top:32px;font-size:8.5px;line-height:12px;color:var(--muted);width:210px}
.post p span{color:var(--red)}
.post-sep{position:absolute;left:90px;top:140px;width:296px;height:1px;background:var(--line)}
.col-sep{position:absolute;left:408px;top:20px;width:1px;height:200px;background:#eee}
.avatar{position:absolute;left:434px;top:64px;width:63px;height:63px;border-radius:50%;border:3px solid var(--red);background:linear-gradient(#c9b8a8,#8d7c70)}
.person{position:absolute;left:514px;top:81px;font-size:10px;font-weight:700;color:var(--darker)}
.person small{display:block;color:var(--red);font-size:8.5px;margin-top:3px}
.quote{position:absolute;left:434px;top:140px;width:296px;font-size:9px;font-style:italic;line-height:17.5px;color:var(--muted);padding-left:6px}
.quote::before{content:"\201C";font-family:Georgia,serif;font-size:26px;color:#bbb;position:absolute;left:-2px;top:-2px;font-style:normal}
.quote span{padding-left:20px}

/* footer */
.site-footer{height:155px;background:var(--footer);position:relative;color:#ddd}
.fcol{position:absolute;top:13px}
.fcol h5{font-size:12px;font-weight:700;color:#fff;padding-bottom:8px;border-bottom:1px solid #3a3a3a;margin-bottom:6px}
.fsep{position:absolute;top:18px;width:1px;height:120px;background:#3a3a3a}
.links{list-style:none;font-size:8.8px;line-height:18px}
.links li::before{content:"\2192";color:var(--red);margin-right:12px}
.links li.active{color:var(--red)}
.fcol p{font-size:8.8px;line-height:13px}
.email-field{width:141px;height:17px;background:#fff;border:1px solid #bbb;color:#555;font-size:8.5px;padding:3px 5px;margin-top:20px}
.subscribe{display:inline-block;margin-top:14px;background:var(--red);color:#fff;font-size:10px;font-weight:700;padding:4px 10px;border:1px solid #fff}
.footer-brand{position:absolute;left:614px;top:60px;font-size:26px;font-weight:700;color:#5a5a5a;display:flex;align-items:center;gap:6px}
.footer-brand i{width:8px;height:8px;background:#5a5a5a;border-radius:50%}
.socials{position:absolute;left:616px;top:130px;display:flex;gap:7px}
.socials span{width:19px;height:19px;border-radius:50%;background:#fff}
.socials span.red{background:var(--red)}
.copyright{height:26px;background:#333;text-align:center;font-size:8.8px;color:#ddd;line-height:28px}
</style>
</head>
<body>

<header class="site-header">
  <div class="brand">
    <div class="brand-name"><i></i>qvlx7.com</div>
    <div class="brand-sub">Ardell, Brant, Corwin &amp; Kade</div>
  </div>
  <div class="phone">
    <svg width="17" height="17" viewBox="0 0 17 17"><circle cx="8.5" cy="8.5" r="7.5" fill="none" stroke="#ec1f27" stroke-width="1.5"/><path d="M5.5 5c.6-.6 1.1-.5 1.4 0l.8 1.3c.2.4 0 .8-.3 1 .4 1 1.2 1.8 2.2 2.2.2-.3.6-.5 1-.3l1.3.8c.5.3.6.8 0 1.4-1.4 1.3-4-.2-5.3-1.6C5.2 8.5 4 6.4 5.5 5z" fill="#ec1f27"/></svg>
    123-456-7890
  </div>
  <nav class="main-nav">
    <a class="active">Home</a>
    <a>Industry Specialties</a>
    <a>Solutions</a>
    <a>Case Studies &amp; Testimonials</a>
    <a>Blog</a>
    <a>Contact Us</a>
  </nav>
</header>

<section class="hero" role="img" aria-label="Photograph of a modern glass airport terminal with airliners at dusk">
  <div class="hero-caption">We Are An Industry Leader In Providing Solutions For Airlines,<br>Air Traffic Control And Communities.</div>
  <div class="dots"><span class="on"></span><span></span><span></span><span></span></div>
</section>

<section class="welcome">
  <div class="welcome-text">
    <h1 class="section-title">Welcome to <b>qvlx7.com</b></h1>
    <p class="lead">Lorem ipsum dolor sit amet, consectetur adipiscing elit. Nulla in sollicitudin</p>
    <p class="body">Lorem ipsum dolor sit amet, consectetur adipiscing elit. Nulla in sollicitudin velit, bibendum velit. Cras vel facilisis ipsum, et venenatis risus. In egestas nunc etvb eros auctor sollicitu Etiam ut enim vitae magna volutpat venenatis vitae nonprof diam. Nam nunc velit, tristique a sapien euismod, pulvinar vestibulum dui. Morbi porttitor eu erat imperdiet pretium consequat fcilelis.</p>
    <span class="btn-red">Read More</span>
  </div>
  <div class="video" role="img" aria-label="Video still of a control tower and a small plane against an orange sunset">
    <div class="play"></div>
    <div class="controls">
      <svg width="7" height="8"><path d="M0 0L7 4L0 8z" fill="#fff"/></svg>
      <svg width="9" height="8"><path d="M0 2.5h2.5L5 0v8L2.5 5.5H0z" fill="#fff"/></svg>
      <div class="bar"><i></i></div>
      <svg width="8" height="8"><path d="M0 8L3 5M8 0L5 3M5 0h3v3M0 5v3h3" stroke="#fff" fill="none"/></svg>
    </div>
  </div>
</section>

<section class="services">
  <h2 class="services-title">Our <b>Services</b></h2>
  <div class="svc-divider" style="left:251px"></div>
  <div class="svc" style="left:270px;width:145px">
    <div class="svc-icon"><svg width="28" height="28" viewBox="0 0 28 28" fill="none" stroke="#bbb" stroke-width="1.5"><circle cx="14" cy="15" r="10" stroke-dasharray="4 2"/><circle cx="14" cy="15" r="5"/><path d="M14 12v3h2"/></svg></div>
    Total System Design<br>&amp; Implementation
  </div>
  <div class="svc-divider" style="left:420px"></div>
  <div class="svc" style="left:430px;width:165px">
    <div class="svc-icon"><svg width="28" height="28" viewBox="0 0 28 28" fill="none" stroke="#bbb" stroke-width="1.5"><path d="M4 4v18h12"/><path d="M7 17l4-5 3 3 4-6"/><circle cx="19" cy="18" r="4"/><path d="M22 21l3 3"/></svg></div>
    Individual Element Design<br>&amp; Implementation
  </div>
  <div class="svc-divider" style="left:607px"></div>
  <div class="svc" style="left:615px;width:125px">
    <div class="svc-icon"><svg width="28" height="28" viewBox="0 0 28 28" fill="none" stroke="#bbb" stroke-width="1.5"><circle cx="14" cy="15" r="9"/><path d="M5 15h18M14 6c-4 5-4 13 0 18M14 6c4 5 4 13 0 18"/><path d="M18 5l5 3-3 1z" fill="#bbb"/></svg></div>
    FAA Coordination<br>&amp; Representation
  </div>
</section>

<section class="inquiry">
  <h2>Quick <b>Inquiry</b></h2>
  <div class="field" style="left:90px;width:141px">Name</div>
  <div class="field" style="left:244px;width:141px">Email</div>
  <div class="field" style="left:399px;width:180px">Message</div>
  <div class="submit">Submit</div>
</section>

<section class="lower">
  <div class="col-head" style="left:90px;width:298px">
    <svg width="28" height="22" viewBox="0 0 28 22"><ellipse cx="11" cy="9" rx="10" ry="7.5" fill="#ec1f27"/><path d="M4 14l-2 6 6-4z" fill="#ec1f27"/><ellipse cx="19" cy="13" rx="8" ry="6" fill="#fff" stroke="#ec1f27" stroke-width="1.5"/></svg>
    <span>Latest <b>Blog</b></span>
    <span class="arrows">‹›</span>
  </div>
  <article class="post" style="top:64px">
    <div class="thumb" role="img" aria-label="Photo of passengers at an airport check-in hall" style="background:linear-gradient(#6d8fb6,#b9c6d2)"></div>
    <h4>Ut tellus dolor, dapibus smit dollar nomk egemop</h4>
    <div class="date">18.02.2016</div>
    <p>Utm tellus dolor, dapibus eget, elemen velmki cursu eleifelitas. Aenean auctorbni wisi et urnam. Aliquam at volutpatis <span>[...]</span></p>
  </article>
  <div class="post-sep"></div>
  <article class="post" style="top:154px">
    <div class="thumb" role="img" aria-label="Aerial view of flight paths over green hills" style="background:linear-gradient(135deg,#3f5a3c,#7c8b6a)"></div>
    <h4>Ut tellus dolor, dapibus smit dollar nomk egemop</h4>
    <div class="date">18.02.2016</div>
    <p>Utm tellus dolor, dapibus eget, elemen velmki cursu eleifelitas. Aenean auctorbni wisi et urnam. Aliquam at volutpatis <span>[...]</span></p>
  </article>
  <div class="col-sep"></div>
  <div class="col-head" style="left:434px;width:296px">
    <svg width="26" height="22" viewBox="0 0 26 22"><rect x="1" y="4" width="17" height="16" rx="2" fill="none" stroke="#ec1f27" stroke-width="2"/><path d="M9 14l2-4 9-9 3 3-9 9z" fill="#333"/></svg>
    <span>Client <b>Testimonials</b></span>
    <span class="arrows">‹›</span>
  </div>
  <div class="avatar" role="img" aria-label="Portrait photo of the client"></div>
  <div class="person">Mr. John Doe<small>Business Man</small></div>
  <p class="quote"><span>Utm tellus dolor, dapibus eget, elemen velmki cursus eleifelita arnean auctorbni wisi et urnam. Lorem ipsum dolor sit amet, conse ctetur adipiscing elit. Nulla in sollicitudin velit, bibendum velit. Cras vel facilisis ipsum, et venenatis risus.</span></p>
</section>

<footer class="site-footer">
  <div class="fcol" style="left:90px;width:133px">
    <h5>Quick Links</h5>
    <ul class="links">
      <li class="active">Home</li>
      <li>Industry Specialties</li>
      <li>Solutions</li>
      <li>Case Studies &amp; Testimonials</li>
      <li>Blog</li>
      <li>Contact Us</li>
    </ul>
  </div>
  <div class="fsep" style="left:243px"></div>
  <div class="fcol" style="left:263px;width:128px">
    <h5>Contact Details</h5>
    <p>qvlx7.com<br>16 Lorem ipsum dolor sit amet sed benetion, Street no-123456</p>
    <p style="margin-top:14px">☏&nbsp; 123-456-7890</p>
    <p style="margin-top:18px">✉&nbsp; info@qvlx7.com</p>
  </div>
  <div class="fsep" style="left:411px"></div>
  <div class="fcol" style="left:431px;width:142px">
    <h5>Newsletter Signup</h5>
    <p style="font-size:10px;line-height:14px">Get latest updates by entering your email address</p>
    <div class="email-field">Email Address</div>
    <span class="subscribe">SUBSCRIBE</span>
  </div>
  <div class="fsep" style="left:593px"></div>
  <div class="footer-brand"><i></i>qvlx7</div>
  <div class="socials"><span></span><span class="red"></span><span></span><span></span></div>
</footer>
<div class="copyright">Copyright © 2016 qvlx7.com. All Rights Reserved.</div>

</body>
</html>
```